Poster Design Project

Our goal is to cover the front of our unit with advertising posters relating to the work that we undertake.
I have attached a photo showing the front of the unit.
Our intention is to cover the windows with a single piece of sheet metal and have these posters digitally printed and applied to the sheet of metal. Just to clarify, no glass and frames of the window will not be visible, they will be completely covered by the posters.
The task is to design 4 x large posters and 1 x small poster to cover all windows to the front of the unit.
At the moment, we only have the dimensions of the sheet metal that will cover the large windows, this being 2150mm (W) x 2550 mm (H).
The dimensions of the small window will follow.
Please take some inspiration from our website as to how we like these posters to look. Generally speaking, a darker background with lighter font will make the poster more legible.
High definition pictures of the work we have done have been attached.
Contact details can be found on our website, although the address will be 47 Harrowgate Lane, Slough, SL3 7DN. Telephone and email stay the same.
We would like facebook and twitter logos to appear on the boards also.
Layout (when looking at attached photo of front of unit):
- furthest left board to have contact details, facebook and twitter logos
- second from the left to advertise our wheel refurbishment services with associated pictures
-second from the right to advertise our window tinting services with associated pictures
- furthest to the right to have contact details, facebook and twitter logos
- window at the top to have our small "nb" logo
Opening hours also to be featured on boards showing contact details: Mon-Sat 8.30am - 5.30pm
The idea of the posters is to capture the attention of people driving by. Hence the posters must portray maximum amount of information in little time
Window Tinting

```html
<!DOCTYPE html>
<html lang="en">
<head>
<meta charset="utf-8">
<title>Window Tinting Services – Northbay Motors</title>
<link href="https://fonts.googleapis.com/css2?family=Lato:wght@700;900&display=swap" rel="stylesheet">
<style>
  :root {
    --blue: #2b6aa6;
    --blue-light: #4a87bf;
    --blue-mid: #3a79b4;
    --red: #c0393d;
    --red-light: #d05a5c;
    --red-stripe: #e28a8a;
    --white: #ffffff;
    --photo-dark: #2c3036;
  }
  html, body {
    margin: 0;
    padding: 0;
    overflow: hidden;
    background: var(--blue);
  }
  .poster {
    position: relative;
    width: 927px;
    height: 1200px;
    overflow: hidden;
    background: var(--blue);
    font-family: "Lato", sans-serif;
  }
  .stripe { position: absolute; top: 0; height: 100%; }
  .stripe--band { left: 383px; width: 100px; background: var(--blue-mid); }
  .stripe--thin-a { left: 354px; width: 9px; background: var(--blue-light); }
  .stripe--thin-b { left: 372px; width: 11px; background: var(--blue-light); }

  .headline-panel {
    position: absolute;
    left: 483px;
    top: 0;
    width: 421px;
    height: 1200px;
    background: var(--red);
  }
  .headline-panel .accent { position: absolute; top: 0; height: 100%; }
  .accent--band { left: 0; width: 60px; background: var(--red-light); }
  .accent--line-a { left: 10px; width: 6px; background: var(--red-stripe); opacity: .6; }
  .accent--line-b { left: 88px; width: 6px; background: var(--red-light); }
  .accent--line-c { left: 104px; width: 5px; background: var(--red-light); }

  .headline {
    position: absolute;
    left: 0;
    top: 0;
    width: 100%;
    margin: 0;
    color: var(--white);
    font-weight: 700;
    font-size: 43px;
    text-align: center;
  }
  .headline span { position: absolute; left: 0; width: 100%; line-height: 1; }
  .headline .line-1 { top: 152px; }
  .headline .line-2 { top: 242px; }
  .headline .line-3 { top: 360px; text-decoration: underline; text-decoration-thickness: 3px; text-underline-offset: 7px; }
  .headline .line-4 { top: 475px; }

  .photo { position: absolute; }
  .photo--coupe {
    left: 20px; top: 29px; width: 414px; height: 400px;
    background: linear-gradient(180deg, #3b3f45 0%, #e9ecee 30%, #f4f5f6 60%, #6b655c 85%, #4a463f 100%);
  }
  .photo--suv {
    left: 483px; top: 767px; width: 421px; height: 404px;
    background: linear-gradient(180deg, #6f8290 0%, #9fa8ab 35%, #b7b29e 60%, #8f9188 80%, #6f8b4c 100%);
  }

  .brand {
    position: absolute;
    left: 22px;
    top: 918px;
    display: flex;
    align-items: center;
    gap: 14px;
  }
  .brand__mark {
    width: 34px; height: 34px;
    border-radius: 50%;
    background: var(--white);
  }
  .brand__name {
    color: var(--white);
    font-weight: 700;
    font-size: 44px;
    line-height: 1;
  }
</style>
</head>
<body>
<main class="poster">
  <div class="stripe stripe--band"></div>
  <div class="stripe stripe--thin-a"></div>
  <div class="stripe stripe--thin-b"></div>

  <section class="headline-panel">
    <div class="accent accent--band"></div>
    <div class="accent accent--line-a"></div>
    <div class="accent accent--line-b"></div>
    <div class="accent accent--line-c"></div>
    <h1 class="headline">
      <span class="line-1">We Provide</span>
      <span class="line-2">BEST</span>
      <span class="line-3">Window Tinting</span>
      <span class="line-4">Services</span>
    </h1>
  </section>

  <div class="photo photo--coupe" role="img" aria-label="White coupe with tinted windows parked outside the workshop"></div>
  <div class="photo photo--suv" role="img" aria-label="Silver SUV with tinted rear windows parked on a forecourt"></div>

  <div class="brand">
    <div class="brand__mark"></div>
    <div class="brand__name">Northbay Motors</div>
  </div>
</main>
</body>
</html>
```